Heronby Mortgage Capital Business Card

We need a business card design for our mortgage servicing company. In addition to servicing the loans of homeowners, we help homeowners with purchasing their homes and any mortgage refinancing. We would like to see designs that use the colors in the logo attached below (gold-ish yellow and navy blue), and any other design you deem fit! The design should communicate a simpler life with smart mortgages provided by Heronby.

```html
<!DOCTYPE html>
<html lang="en">
<head>
<meta charset="utf-8">
<title>Heronby Mortgage Capital — Business Card</title>
<link rel="stylesheet" href="https://fonts.googleapis.com/css2?family=Arimo:ital,wght@0,400;0,700;1,400&family=Open+Sans:ital,wght@1,400&display=swap">
<style>
  :root {
    --gold: #cfa43a;
    --navy: #2b2a5c;
    --ink: #1f1f24;
    --paper: #f6f6f6;
    --backdrop: #2a2a2c;
  }
  * { box-sizing: border-box; margin: 0; padding: 0; }
  html, body { width: 1200px; height: 768px; overflow: hidden; }
  body {
    background: var(--backdrop);
    font-family: "Arimo", Arial, sans-serif;
    position: relative;
  }
  .card {
    position: absolute;
    top: 224px;
    width: 560px;
    height: 320px;
    border-radius: 24px;
    overflow: hidden;
  }
  .card--back { left: 25px; background: var(--gold); }
  .card--front { left: 615px; background: var(--paper); color: var(--ink); }

  .wordmark {
    display: flex;
    align-items: center;
    gap: 10px;
    color: var(--navy);
    font-weight: 700;
  }
  .wordmark__dot {
    border-radius: 50%;
    background: var(--navy);
  }
  .card--back .wordmark {
    position: absolute;
    left: 0; right: 0; top: 0; bottom: 0;
    justify-content: center;
    font-size: 64px;
  }
  .card--back .wordmark__dot { width: 22px; height: 22px; }
  .card--front .wordmark {
    position: absolute;
    right: 46px;
    top: 74px;
    font-size: 34px;
  }
  .card--front .wordmark__dot { width: 12px; height: 12px; }

  .holder { position: absolute; left: 34px; top: 30px; }
  .holder__name { color: var(--gold); font-weight: 700; font-size: 22px; letter-spacing: 0.3px; }
  .holder__role { color: var(--navy); font-style: italic; font-size: 15px; margin-top: 1px; }

  .tagline {
    position: absolute; left: 34px; top: 196px;
    font-family: "Open Sans", Arial, sans-serif;
    font-style: italic; font-size: 15px; color: var(--navy);
  }
  .divider {
    position: absolute; left: 30px; right: 30px; top: 222px;
    height: 1px; background: var(--ink);
  }
  .address {
    position: absolute; left: 34px; top: 232px;
    font-size: 16px; line-height: 20px;
  }
  .contact {
    position: absolute; right: 30px; top: 196px;
    list-style: none; text-align: right; font-size: 17px;
  }
  .contact li { display: flex; align-items: center; justify-content: flex-end; gap: 10px; height: 22px; }
  .contact li.contact__phone { margin-bottom: 14px; }
  .contact svg { width: 14px; height: 14px; fill: var(--gold); }
</style>
</head>
<body>
  <section class="card card--back" aria-label="Card back">
    <div class="wordmark"><span class="wordmark__dot"></span>Heronby</div>
  </section>

  <section class="card card--front" aria-label="Card front">
    <div class="holder">
      <p class="holder__name">Owen Harlow</p>
      <p class="holder__role">President</p>
    </div>
    <div class="wordmark"><span class="wordmark__dot"></span>Heronby</div>

    <p class="tagline">Simpler life with smart mortgages</p>
    <div class="divider"></div>
    <p class="address">2910 Larkspur Lane<br>Ashford Hills, NY 10990</p>

    <ul class="contact">
      <li class="contact__phone">(555) 0142-7780
        <svg viewBox="0 0 24 24" aria-hidden="true"><path d="M6.6 10.8a15.1 15.1 0 0 0 6.6 6.6l2.2-2.2a1 1 0 0 1 1-.25 11.4 11.4 0 0 0 3.6.57 1 1 0 0 1 1 1V20a1 1 0 0 1-1 1A17 17 0 0 1 3 4a1 1 0 0 1 1-1h3.5a1 1 0 0 1 1 1c0 1.25.2 2.45.57 3.57a1 1 0 0 1-.25 1z"/></svg>
      </li>
      <li>name@Heronby.com
        <svg viewBox="0 0 24 24" aria-hidden="true"><path d="M2 5h20v14H2z M2 5l10 8 10-8" stroke="#f6f6f6" stroke-width="1.5"/></svg>
      </li>
      <li>www.Heronby.com
        <svg viewBox="0 0 24 24" aria-hidden="true"><circle cx="12" cy="12" r="10"/><path d="M2 12h20M12 2c3 3 3 17 0 20M12 2c-3 3-3 17 0 20" stroke="#f6f6f6" stroke-width="1.3" fill="none"/></svg>
      </li>
    </ul>
  </section>
</body>
</html>
```